Surface Protection company needs cards

We are a New Zealand company that will apply nanotechnology coatings on surfaces to prevent growth and spread of bacteria, viruses, mold etc with a sprayer. We deal with large corporates, airlines, hospitals and schools so we are after a new modern, simple and clean look that will have great visual impact.
We a company that is focused on prevention and protection.

Company name, Vela Shield

Subtext, Antimicrobial Surface Protection

Logo, VS

Target Market(s)

Hospitals, Transport agencies, Airlines, Corporate entities

Contact Information for Business Card

Company name, VelaShield
Logo, VS

Gareth Tolley
velashieldnz@postbox.example
+64219305562
www.velashield.example.nz

Requirements
Must have
• Simple clean look.
Nice to have
• We apply nano coatings so try and incorporate this into a theme somehow

```html
<!DOCTYPE html>
<html lang="en">
<head>
<meta charset="utf-8">
<title>VelaShield – Business Card</title>
<link rel="stylesheet" href="https://fonts.googleapis.com/css2?family=Open+Sans:wght@400&family=Roboto+Condensed:wght@500;700&display=swap">
<style>
  :root {
    --ink: #1f2427;
    --ink-soft: #33393d;
    --paper-light: #fbfbfb;
    --paper-mid: #f0f0f0;
    --paper-shade: #e9eaea;
  }
  * { margin: 0; padding: 0; box-sizing: border-box; }
  html, body {
    width: 1200px;
    height: 686px;
    overflow: hidden;
    background: var(--paper-light);
  }
  .card {
    position: relative;
    width: 1200px;
    height: 686px;
    overflow: hidden;
    color: var(--ink);
  }
  .card-texture {
    position: absolute;
    inset: 0;
    background:
      radial-gradient(ellipse at 75% 30%, var(--paper-light) 0%, transparent 60%),
      radial-gradient(ellipse at 20% 80%, var(--paper-shade) 0%, transparent 55%),
      linear-gradient(135deg, var(--paper-mid) 0%, var(--paper-light) 45%, var(--paper-mid) 100%);
  }
  .brand-name {
    position: absolute;
    left: 172px;
    top: 146px;
    font-family: "Roboto Condensed", "Arial Narrow", sans-serif;
    font-weight: 700;
    font-size: 70px;
    letter-spacing: 4.5px;
    line-height: 1;
    color: var(--ink);
  }
  .brand-tagline {
    position: absolute;
    left: 176px;
    top: 222px;
    font-family: "Open Sans", Arial, sans-serif;
    font-weight: 400;
    font-size: 24.5px;
    letter-spacing: -0.2px;
    color: var(--ink-soft);
  }
  .brand-rule {
    position: absolute;
    left: 176px;
    top: 274px;
    width: 65px;
    height: 3px;
    background: var(--ink);
  }
  .brand-mark {
    position: absolute;
    left: 203px;
    top: 455px;
    font-family: "Roboto Condensed", "Arial Narrow", sans-serif;
    font-weight: 700;
    font-size: 76px;
    letter-spacing: 4px;
    line-height: 1;
    color: var(--ink);
  }
  .person-name {
    position: absolute;
    left: 697px;
    top: 352px;
    font-family: "Roboto Condensed", "Arial Narrow", sans-serif;
    font-weight: 700;
    font-size: 50px;
    letter-spacing: 3.5px;
    line-height: 1;
    color: var(--ink);
  }
  .contact-list {
    position: absolute;
    left: 697px;
    top: 428px;
    list-style: none;
  }
  .contact-item {
    display: flex;
    align-items: center;
    height: 43px;
    font-family: "Open Sans", Arial, sans-serif;
    font-size: 24.5px;
    letter-spacing: -0.3px;
    color: var(--ink-soft);
  }
  .contact-icon {
    width: 28px;
    height: 28px;
    margin-right: 33px;
    flex: none;
    fill: var(--ink-soft);
  }
</style>
</head>
<body>
  <div class="card">
    <div class="card-texture" role="img" aria-label="Soft pale grey surface with fine water droplets beading on a nano coating"></div>

    <div class="brand-name">VELASHIELD</div>
    <div class="brand-tagline">Antimicrobial Surface Protection</div>
    <div class="brand-rule"></div>

    <div class="brand-mark">VS</div>

    <div class="person-name">GARETH TOLLEY</div>

    <ul class="contact-list">
      <li class="contact-item">
        <svg class="contact-icon" viewBox="0 0 24 24" aria-hidden="true">
          <path d="M12 2a10 10 0 1 0 0 20 10 10 0 0 0 0-20zm6.9 6h-2.9a15.7 15.7 0 0 0-1.4-3.6A8 8 0 0 1 18.9 8zM12 4a14 14 0 0 1 1.9 4h-3.8A14 14 0 0 1 12 4zM4.3 14a8 8 0 0 1 0-4h3.4a16 16 0 0 0 0 4H4.3zm.8 2h2.9c.3 1.3.8 2.5 1.4 3.6A8 8 0 0 1 5.1 16zM8 8H5.1a8 8 0 0 1 4.3-3.6C8.8 5.5 8.4 6.7 8 8zm4 12a14 14 0 0 1-1.9-4h3.8A14 14 0 0 1 12 20zm2.3-6H9.7a14.7 14.7 0 0 1 0-4h4.6a14.7 14.7 0 0 1 0 4zm.3 5.6c.6-1.100 1.1-2.3 1.4-3.6h2.9a8 8 0 0 1-4.3 3.6zm1.7-5.6a16 16 0 0 0 0-4h3.4a8 8 0 0 1 0 4h-3.4z"/>
        </svg>
        <span>www.velashield.example.nz</span>
      </li>
      <li class="contact-item">
        <svg class="contact-icon" viewBox="0 0 24 24" aria-hidden="true">
          <path d="M6.6 10.8a15.2 15.2 0 0 0 6.6 6.6l2.2-2.2c.3-.3.7-.4 1-.2 1.1.4 2.3.6 3.6.6.6 0 1 .4 1 1V20c0 .6-.4 1-1 1A17 17 0 0 1 3 4c0-.6.4-1 1-1h3.5c.6 0 1 .4 1 1 0 1.300.2 2.500.6 3.600.1.3 0 .7-.2 1l-2.3 2.2z"/>
        </svg>
        <span>+6421 9305 562</span>
      </li>
      <li class="contact-item">
        <svg class="contact-icon" viewBox="0 0 24 24" aria-hidden="true">
          <path d="M20 4H4a2 2 0 0 0-2 2v12a2 2 0 0 0 2 2h16a2 2 0 0 0 2-2V6a2 2 0 0 0-2-2zm0 4-8 5-8-5V6l8 5 8-5v2z"/>
        </svg>
        <span>velashieldnz@postbox.example</span>
      </li>
    </ul>
  </div>
</body>
</html>
```